Exceptional Corporate Business Card Design

Hello,

We need an exceptional corporate business card design based on our logo attached. We require:

1. A Variation for letterpress print
2. Standard size of business card 84mm x 55mm (Artwork 88mm x 59mm)
3. Variation for square business card 65mm x 65mm (Artwork 69mm x 69mm)
4. Variation as a one side print
5. Adobe Illustrator files

The company is in the financial industry, valmisto.com

The logo is attached as vector pdf.
regards

```html
<!DOCTYPE html>
<html lang="en">
<head>
<meta charset="utf-8">
<title>Valmisto Business Card</title>
<link rel="stylesheet" href="https://fonts.googleapis.com/css2?family=Lato:wght@400;700&display=swap">
<style>
  :root {
    --backdrop: #2f2825;
    --brand-blue: #2e2b80;
    --brand-blue-faint: #3a3790;
    --ink-blue: #2a2a86;
    --ink-grey: #6b6b73;
    --paper: #ffffff;
    --coin-light: #c9c8e6;
  }
  html, body {
    margin: 0;
    width: 1200px;
    height: 768px;
    overflow: hidden;
    background: var(--backdrop);
  }
  .canvas {
    position: relative;
    width: 1200px;
    height: 768px;
    font-family: "Lato", sans-serif;
  }
  .card {
    position: absolute;
    top: 210px;
    width: 510px;
    height: 342px;
    box-shadow: 0 10px 24px rgba(0,0,0,0.45);
    overflow: hidden;
  }
  /* Back of card */
  .card-back {
    left: 70px;
    background: var(--brand-blue);
  }
  .card-back .faint-emblem {
    position: absolute;
    left: 60px;
    top: 20px;
    width: 210px;
    height: 210px;
    border-radius: 50%;
    background: var(--brand-blue-faint);
  }
  .brand {
    position: absolute;
    display: flex;
    align-items: center;
    gap: 10px;
    font-weight: 700;
    letter-spacing: 2px;
  }
  .brand-dot {
    border-radius: 50%;
    flex: none;
  }
  .card-back .brand {
    right: 36px;
    bottom: 60px;
    color: var(--paper);
    font-size: 42px;
  }
  .card-back .brand-dot {
    width: 50px;
    height: 50px;
    background: var(--paper);
  }
  /* Front of card */
  .card-front {
    left: 620px;
    background: var(--paper);
  }
  .card-front .brand {
    left: 30px;
    top: 26px;
    color: var(--ink-blue);
    font-size: 28px;
  }
  .card-front .brand-dot {
    width: 36px;
    height: 36px;
    background: var(--ink-blue);
  }
  .identity {
    position: absolute;
    left: 30px;
    top: 82px;
  }
  .identity .name {
    margin: 0;
    font-size: 17px;
    font-weight: 700;
    color: var(--ink-blue);
  }
  .identity .role {
    margin: 2px 0 0;
    font-size: 13px;
    color: var(--ink-grey);
  }
  .contact-list {
    position: absolute;
    left: 30px;
    top: 140px;
    margin: 0;
    padding: 0;
    list-style: none;
    font-size: 13px;
    color: var(--ink-grey);
  }
  .contact-list li {
    display: flex;
    align-items: center;
    gap: 7px;
    height: 19px;
  }
  .contact-list svg {
    width: 12px;
    height: 12px;
    fill: none;
    stroke: var(--ink-blue);
    stroke-width: 1.6;
  }
  .address {
    position: absolute;
    left: 30px;
    top: 210px;
    margin: 0;
    font-size: 13px;
    line-height: 1.35;
    color: var(--ink-grey);
    font-style: normal;
  }
  .coin-emblem {
    position: absolute;
    right: 30px;
    top: 110px;
    width: 200px;
    height: 200px;
    border-radius: 50%;
    border: 6px solid var(--ink-blue);
    background: radial-gradient(circle at 45% 40%, var(--coin-light), var(--ink-blue));
    box-sizing: border-box;
  }
</style>
</head>
<body>
  <main class="canvas">
    <section class="card card-back" aria-label="Card back">
      <div class="faint-emblem" role="img" aria-label="Faint classical coin emblem decoration"></div>
      <div class="brand"><span class="brand-dot"></span>VALMISTO</div>
    </section>

    <section class="card card-front" aria-label="Card front">
      <div class="brand"><span class="brand-dot"></span>VALMISTO</div>
      <div class="identity">
        <p class="name">Daniel Harlow</p>
        <p class="role">Director</p>
      </div>
      <ul class="contact-list">
        <li>
          <svg viewBox="0 0 12 12" aria-hidden="true"><rect x="3" y="1" width="6" height="10" rx="1"/></svg>
          1 23 555 01482
        </li>
        <li>
          <svg viewBox="0 0 12 12" aria-hidden="true"><rect x="1" y="2.5" width="10" height="7"/><path d="M1 2.5 L6 7 L11 2.5"/></svg>
          admin@valmisto.com
        </li>
        <li>
          <svg viewBox="0 0 12 12" aria-hidden="true"><circle cx="6" cy="6" r="5"/><path d="M1 6 H11 M6 1 C3 4 3 8 6 11 M6 1 C9 4 9 8 6 11"/></svg>
          www.valmisto.com
        </li>
      </ul>
      <address class="address">St. 48, Opposite River Plaza,<br>NY 4411</address>
      <div class="coin-emblem" role="img" aria-label="Classical coin illustration in blue"></div>
    </section>
  </main>
</body>
</html>
```